Need Business Card ASAP

We need a business card design for a meeting coming up in a few days. The company name is Harwick Development and Construction and the logo is attached. Something clean, cool, and contemporary that we can get to a printer right away. Attached is the business card for Molvar Energy, an affiliated company, which we like. Instead of the hawk on the back, you could use the attached "D". We'll also be needing matching letterhead in the near future, so ideas for that are welcome.

```html
<!DOCTYPE html>
<html lang="en">
<head>
<meta charset="utf-8">
<title>Harwick Development &amp; Construction — Business Cards</title>
<link href="https://fonts.googleapis.com/css2?family=Roboto+Condensed:wght@400;700&display=swap" rel="stylesheet">
<style>
  :root {
    --board: #f6f6f6;
    --card-white: #ffffff;
    --card-black: #231f20;
    --gold: #bcb27a;
    --gold-light: #d8d2ac;
    --ink: #231f20;
    --rule: #8a8a8a;
    --divider: #c8c8c8;
  }
  * { margin: 0; padding: 0; box-sizing: border-box; }
  html, body { width: 1200px; height: 900px; overflow: hidden; }
  body {
    background: var(--board);
    font-family: "Roboto Condensed", "Arial Narrow", sans-serif;
    color: var(--ink);
    position: relative;
  }
  .card {
    position: absolute;
    width: 401px;
    height: 228px;
    box-shadow: 0 4px 8px rgba(0,0,0,0.28);
  }
  .card--front { background: var(--card-white); }
  .card--back { background: var(--card-black); }
  .card > * { position: absolute; }

  .board-divider {
    position: absolute;
    left: 130px; top: 450px;
    width: 942px; height: 1px;
    background: var(--divider);
  }

  .person-name {
    font-weight: 700; font-size: 21px; color: var(--gold);
    letter-spacing: 0.2px; line-height: 1; white-space: nowrap;
  }
  .person-title { font-size: 10.5px; line-height: 1; white-space: nowrap; }
  .company-name { font-weight: 700; font-size: 12px; line-height: 1; white-space: nowrap; }
  .company-address { font-size: 11px; line-height: 1; white-space: nowrap; }
  .contact-line { font-size: 11px; line-height: 1; white-space: nowrap; }
  .contact-line b { font-weight: 700; }
  .web-address { font-size: 11px; color: var(--gold); line-height: 1; white-space: nowrap; }
  .card-rule { height: 1px; background: var(--rule); }

  .brand-square { background: linear-gradient(135deg, var(--gold), var(--gold-light)); }
  .brand-name {
    color: var(--gold); font-weight: 400; line-height: 1; white-space: nowrap;
  }
</style>
</head>
<body>

  <!-- Row 1: front -->
  <section class="card card--front" style="left:168px; top:154px;">
    <div class="person-name" style="left:28px; top:60px;">MARTIN L CRANE</div>
    <div class="person-title" style="left:28px; top:83px;">Managing Director</div>
    <div class="company-name" style="left:28px; top:113px;">Harwick Development &amp; Construction</div>
    <div class="company-address" style="left:28px; top:128px;">2210 W. 41st St. Austin, TX 78756</div>
    <div class="card-rule" style="left:28px; top:150px; width:345px;"></div>
    <div class="contact-line" style="left:28px; top:163px;"><b>P</b> (512) 555-0142 &nbsp;<b>F</b> (512) 555-0148</div>
    <div class="contact-line" style="left:28px; top:178px;"><b>E</b> info@harwickdevelopment.com</div>
    <div class="web-address" style="right:28px; top:178px;">www.harwickdevelopment.com</div>
    <div class="brand-square" style="left:298px; top:40px; width:62px; height:62px;"></div>
    <div class="brand-name" style="left:298px; top:110px; font-size:17px;">Harwick</div>
  </section>

  <!-- Row 1: back -->
  <section class="card card--back" style="left:632px; top:154px;">
    <div class="brand-square" style="left:150px; top:44px; width:100px; height:100px;"></div>
    <div class="brand-name" style="left:0; width:401px; text-align:center; top:156px; font-size:26px;">Harwick</div>
  </section>

  <div class="board-divider"></div>

  <!-- Row 2: back -->
  <section class="card card--back" style="left:169px; top:516px;">
    <div class="brand-square" style="left:150px; top:44px; width:100px; height:100px;"></div>
    <div class="brand-name" style="left:0; width:401px; text-align:center; top:156px; font-size:26px;">Harwick</div>
  </section>

  <!-- Row 2: front -->
  <section class="card card--front" style="left:633px; top:516px;">
    <div class="brand-square" style="left:27px; top:40px; width:46px; height:46px;"></div>
    <div class="brand-name" style="left:84px; top:52px; font-size:22px;">Harwick</div>
    <div class="company-name" style="left:214px; top:51px; font-size:11px;">Harwick Development &amp; Construction</div>
    <div class="company-address" style="left:214px; top:65px;">2210 W. 41st St. Austin, TX 78756</div>
    <div class="person-name" style="left:27px; top:109px; font-size:19px;">MARTIN L CRANE</div>
    <div class="person-title" style="left:27px; top:130px;">Managing Director</div>
    <div class="card-rule" style="left:27px; top:151px; width:346px;"></div>
    <div class="contact-line" style="left:27px; top:164px;"><b>P</b> (512) 555-0142 &nbsp;<b>F</b> (512) 555-0148</div>
    <div class="contact-line" style="left:27px; top:178px;"><b>E</b> info@harwickdevelopment.com</div>
    <div class="web-address" style="left:214px; top:178px;">www.harwickdevelopment.com</div>
  </section>

</body>
</html>
```